Dietitian needs a new business card design

I need a new business card design for my nutrition business that provides individual clinical nutrition advice for people with medical conditions. Business cards will be handed out to doctors, specialists and clients so will need to be sharp and project an image of professionalism

Target Market(s)

My clients are typically referred by doctors or specialists and the card will be used to handout to clients and their doctors.

Industry/Entity Type

Medical

Contact Information for Business Card

The business card will require the details below. These details can be found from my website https://www.kelvarrowclinic.com.au/

Font styles to use
Serif

Colors

Designer to choose colors to be used in the design.

Requirements
Must have
• 1. It needs be professional and contemporary
• 2. It needs to incorporate my logo
• 3. It needs space to write appointment times and dates
• 4. It needs to provide my phone number, fax number, email address and my web address
Nice to have
• Include the Registered Tovance Clinician Logo
• I have access to Framellow if required
• The locations I practise from
Should not have
• Pictures of food
• Spelling MIstakes

```html
<!DOCTYPE html>
<html lang="en">
<head>
<meta charset="utf-8">
<title>Martin Ellwood – Business Card</title>
<link rel="stylesheet" href="https://fonts.googleapis.com/css2?family=Merriweather:wght@700&family=Arimo:wght@400&display=swap">
<style>
  :root {
    --brand-blue: #0b5fb0;
    --band-start: #0052a3;
    --band-end: #00a2e2;
    --badge-orange: #f47a20;
    --logo-green: #c9e49c;
    --paper: #ffffff;
    --white: #ffffff;
  }
  * { margin: 0; padding: 0; box-sizing: border-box; }
  html, body { width: 1200px; height: 720px; overflow: hidden; background: var(--paper); }
  .card {
    position: relative;
    width: 1200px;
    height: 720px;
    background: var(--paper);
    color: var(--brand-blue);
    font-family: "Arimo", Arial, sans-serif;
  }
  .brand-mark {
    position: absolute;
    left: 90px;
    top: 75px;
    width: 320px;
    display: flex;
    flex-direction: column;
    align-items: center;
    gap: 22px;
  }
  .brand-mark__circle {
    width: 320px;
    height: 320px;
    border-radius: 50%;
    background: var(--logo-green);
  }
  .brand-mark__name {
    font-family: "Merriweather", Georgia, serif;
    font-weight: 700;
    font-size: 32px;
    color: var(--brand-blue);
    white-space: nowrap;
  }
  .identity {
    position: absolute;
    right: 61px;
    top: 70px;
    text-align: right;
  }
  .identity__name {
    font-family: "Merriweather", Georgia, serif;
    font-weight: 700;
    font-size: 66px;
    line-height: 1.1;
    letter-spacing: 1px;
    color: var(--brand-blue);
    text-shadow: 1px 2px 2px rgba(0, 40, 90, 0.25);
  }
  .identity__role {
    margin-top: 14px;
    font-size: 30px;
    line-height: 1.2;
  }
  .credential-badge {
    display: inline-block;
    margin-top: 16px;
    width: 98px;
    height: 46px;
    border-radius: 2px;
    background: var(--badge-orange);
  }
  .contact {
    position: absolute;
    right: 61px;
    top: 330px;
    display: grid;
    grid-template-columns: auto auto;
    column-gap: 18px;
    row-gap: 14px;
    font-size: 28px;
    line-height: 1.3;
    text-align: right;
  }
  .contact__label { text-align: right; }
  .contact__value { text-align: right; }
  .contact__email { grid-column: 1 / span 2; font-size: 26px; }
  .services-band {
    position: absolute;
    left: 0;
    top: 517px;
    width: 1200px;
    height: 110px;
    background: linear-gradient(90deg, var(--band-start), var(--band-end));
    display: flex;
    align-items: center;
    padding-left: 62px;
  }
  .services-band__list {
    color: var(--white);
    font-size: 28.5px;
    white-space: nowrap;
  }
  .website {
    position: absolute;
    left: 0;
    width: 1168px;
    top: 652px;
    text-align: center;
    font-size: 29px;
  }
</style>
</head>
<body>
  <main class="card">
    <div class="brand-mark">
      <div class="brand-mark__circle"></div>
      <div class="brand-mark__name">Kelvarrow Clinic</div>
    </div>

    <header class="identity">
      <h1 class="identity__name">Martin Ellwood</h1>
      <p class="identity__role">Accredited Nutritionist | Qualified Chef</p>
      <span class="credential-badge" role="img" aria-label="Registered Tovance Clinician badge"></span>
    </header>

    <section class="contact">
      <span class="contact__label">Phone:</span>
      <span class="contact__value">0412 555 019</span>
      <span class="contact__label">Fax:</span>
      <span class="contact__value">+613 6390 4417</span>
      <span class="contact__email">martin@kelvarrowclinic.com.au</span>
    </section>

    <div class="services-band">
      <p class="services-band__list">Chronic Disease Management Plans | Nutrition Solutions | Corporate Nutrition Consulting</p>
    </div>

    <p class="website">www.kelvarrowclinic.com.au</p>
  </main>
</body>
</html>
```